Bref créative
VERANTIX Stationary
Business Cards, A4 Letterhead, DL Envelope, C4 Envelope, C5 Envelope, PPT Template, File
Professional
Tariq H. Al Zubaidi
P.O. Box 67812
Jeddah, 23687
Saudi Arabia
tzubaidi@verantix-example.com
www.verantix-example.com
Our company is an Agricultural Solutions Company.
When designing think along the lines of Consulting, innovation, professional, B2B dealing. I don't want designs that are too "farmy" - if you well. Think of us as the corporate office people of the Agricultural industry.
The stationary should be bilingual English and Arabic.
The Arabic text for the address and contact information is as follows.
Tariq H Al Zubaidi = طارق حسين الزبيدي
Partner = شريك
P. O. Box = ص. ب
Jeddah = جدة
Saudi Arabia = المملكة العربية السعودية
Numbers are the same in both languages.
I ask the designer to use best judgment in selecting the font to be used on the card.
On the letterhead, we prefer the address and contact information be on the bottom of the page to accommodate for having both languages without making the letterhead busy.
On the business card, I generally do not like large centered logos.
I would like to see some innovative designs on the business card.
Back of the business card should be the mirror image of the front. This is a sample of what it I mean
Arabic is a right to left language, so please take that in consideration when designing.
Arabic Abriviations:
T = هـ
F = ف
M = ج
Words:
Tel = هاتف
Fax = فاكس
Mobile = جوال
email = بريد إلكتروني
Verantix Logo
This file contains two Arabic fonts a normal one and a bold one.

```html
<!DOCTYPE html>
<html lang="en">
<head>
<meta charset="utf-8">
<title>Verantix Stationery</title>
<link href="https://fonts.googleapis.com/css2?family=Open+Sans:wght@400;600;700&family=Cairo:wght@400;700&display=swap" rel="stylesheet">
<style>
  :root{
    --paper:#ffffff;
    --canvas:#ffffff;
    --edge:#c9c9c9;
    --green:#4c9b2f;
    --green-light:#7cc242;
    --navy:#1f3a5c;
    --blue:#2b9fd8;
    --blue-light:#7fd0f2;
    --brown-dark:#3b2314;
    --brown:#7a5030;
    --brown-light:#a3734b;
    --ink:#3a3a3a;
  }
  *{margin:0;padding:0;box-sizing:border-box}
  html,body{width:1200px;height:871px;overflow:hidden;background:var(--canvas)}
  body{position:relative;font-family:"Open Sans",Arial,sans-serif;color:var(--ink)}
  .sheet{position:absolute;background:var(--paper);border:1px solid var(--edge)}
  .brand{position:absolute;line-height:1}
  .brand-name{font-weight:700;color:var(--green);display:block;letter-spacing:.2px}
  .brand-ar{font-family:"Cairo",sans-serif;font-weight:700;color:var(--navy);display:block;direction:rtl;text-align:left;line-height:1.1}
  .brand-tag{font-weight:700;color:var(--navy);display:block;white-space:nowrap}
  .contact{position:absolute;font-size:6px;line-height:1.45;color:var(--ink);white-space:nowrap}
  .contact.ar{font-family:"Cairo",sans-serif;direction:rtl;text-align:right}
  .band{position:absolute;left:0;right:0}
  .band-blue{background:linear-gradient(180deg,var(--blue-light),var(--blue))}
  .band-green{background:linear-gradient(180deg,var(--green-light),var(--green))}
  .band-brown{background:linear-gradient(90deg,var(--brown-dark),var(--brown) 35%,var(--brown-light) 55%,var(--brown) 75%,var(--brown-dark))}
  .fold{position:absolute;top:0;bottom:0;left:323px;border-left:1px dashed #b8b8b8}
</style>
</head>
<body>

<!-- Letterhead, small view -->
<section class="sheet letterhead-small" style="left:12px;top:36px;width:449px;height:533px">
  <div class="brand" style="left:20px;top:14px">
    <span class="brand-name" style="font-size:28px">Verantix</span>
    <span class="brand-ar" style="font-size:8px;width:110px">الحلول الزراعية الحديثة</span>
    <span class="brand-tag" style="font-size:5.5px">Modern Agricultural Solutions</span>
  </div>
  <div class="contact" style="left:218px;top:18px;font-size:5px">
    P.O. Box 67812<br>Jeddah, 23687<br>Saudi Arabia<br>T +966 12 600 0000<br>F +966 12 600 0001<br>www.verantix-example.com
  </div>
  <div class="contact ar" style="left:296px;top:18px;width:80px;font-size:5px">
    ص. ب 67812<br>جدة 23687<br>المملكة العربية السعودية<br>هـ 0000 600 12 966+<br>ف 0001 600 12 966+
  </div>
  <div class="band band-blue" style="top:494px;height:4px"></div>
  <div class="band band-green" style="top:500px;height:6px"></div>
  <div class="band band-brown" style="top:508px;height:24px"></div>
</section>

<!-- Business card, front -->
<section class="sheet card-front" style="left:24px;top:576px;width:211px;height:106px">
  <div class="brand" style="left:8px;top:10px">
    <span class="brand-name" style="font-size:17px">Verantix</span>
    <span class="brand-tag" style="font-size:4px">Modern Agricultural Solutions</span>
  </div>
  <div class="contact" style="left:104px;top:12px;font-size:4.5px">
    <b style="font-size:5.5px">Tariq H. Al Zubaidi</b><br>Partner<br>M +966 50 000 0000<br>T +966 12 600 0000<br>tzubaidi@verantix-example.com
  </div>
  <div class="band band-blue" style="top:76px;height:2px"></div>
  <div class="band band-green" style="top:79px;height:3px"></div>
  <div class="band band-brown" style="top:83px;height:22px"></div>
</section>

<!-- Business card, back (Arabic) -->
<section class="sheet card-back" style="left:271px;top:576px;width:193px;height:106px">
  <div class="brand" style="left:8px;top:10px">
    <span class="brand-name" style="font-size:17px">Verantix</span>
    <span class="brand-ar" style="font-size:5px;width:70px">الحلول الزراعية الحديثة</span>
  </div>
  <div class="contact ar" style="left:90px;top:10px;width:95px;font-size:4.5px">
    <b style="font-size:5.5px">طارق حسين الزبيدي</b><br>شريك<br>ج 0000 000 50 966+<br>هـ 0000 600 12 966+<br>ص. ب 67812 جدة 23687
  </div>
  <div class="band band-blue" style="top:76px;height:2px"></div>
  <div class="band band-green" style="top:79px;height:3px"></div>
  <div class="band band-brown" style="top:83px;height:22px"></div>
</section>

<!-- Letterhead spread, large view -->
<section class="sheet letterhead-spread" style="left:473px;top:36px;width:720px;height:643px">
  <div class="fold"></div>
  <div class="brand" style="left:512px;top:17px">
    <span class="brand-name" style="font-size:42px">Verantix</span>
    <span class="brand-ar" style="font-size:11px;width:170px">الحلول الزراعية الحديثة</span>
    <span class="brand-tag" style="font-size:8px">Modern Agricultural Solutions</span>
  </div>

  <div class="contact" style="left:16px;top:552px">
    P.O. Box 67812<br>Jeddah, 23687<br>Saudi Arabia<br><br>T&nbsp;&nbsp;+966 12 600 0000<br>F&nbsp;&nbsp;+966 12 600 0001<br>E&nbsp;&nbsp;www.verantix-example.com
  </div>
  <div class="contact ar" style="left:200px;top:550px;width:115px">
    ص. ب 67812<br>جدة 23687<br>المملكة العربية السعودية<br>هاتف 0000 600 12 966+<br>فاكس 0001 600 12 966+<br>بريد إلكتروني www.verantix-example.com
  </div>

  <div style="position:absolute;left:324px;right:0;top:0;bottom:0">
    <div class="band band-blue" style="top:521px;height:10px"></div>
    <div class="band band-green" style="top:534px;height:18px"></div>
    <div class="band band-brown" style="top:556px;height:86px"></div>
  </div>
</section>

</body>
</html>
```